Formlantic Banner Ads

OVERVIEW:

Formlantic is an on-demand, data capture solution that transforms paper, pdf and fax forms into machine readable data with 99% accuracy. Our mission is to unlock the data that drives the world forward. For everyone. We make data capture, easy, affordable and useful for everyone.

These ads should be elegant, professional and convey as sense of how new and different our technology is. We are truly a disruptive solution. Easy to use, fast and highly accurate.

The project is a series of two animated banner ads. These will be displayed on the web as part of our SEM.

Please visit our site (www.formlantic-demo.com) to see our branding, colors and style.

I have attached two versions of our logo.

SPECS:
Each ad should be animated, with two screens and be delivered as a .gif not to exceed 150KB in size for each ad.

Each ad needs to be produced in FOUR sizes. These are:

728x90, 336x280, 120x600 and 300x600

So it is a TOTAL of 8 different ads, each not to exceed 105 KB and each delivered as a .gif.

COPY:

[Ad #1]
Capture data from handwritten forms.

Simple, web-based solution digitizes data, fast. 99% accurate. Free Trial (button)

[Ad #2]

Manage your paper backlog and free your data.

Simple, web-based solution digitizes handwritten forms. Free Trial (button)

Target Market(s)

The target audience is a decision maker in an operations role or a project manager.

Requirements
Must have
• Each ad must not exceed 150 KB in total size.

```html
<!DOCTYPE html>
<html lang="en">
<head>
<meta charset="utf-8">
<title>Formlantic Banner Ads</title>
<link href="https://fonts.googleapis.com/css2?family=Arimo:wght@400;700&display=swap" rel="stylesheet">
<style>
:root{
  --page:#ffffff;
  --sky:#35b3e8;
  --sky-deep:#1f93d3;
  --leaf:#dcebc4;
  --paper:#ffffff;
  --ink-title:#2c4d70;
  --panel:#58595b;
  --panel-text:#7cf1ee;
  --ribbon:#f26c1c;
  --ribbon-dark:#c9500f;
  --base:#2a67ab;
  --base-deep:#1f5696;
  --rim:#b9bfc7;
  --btn-top:#b5e25a;
  --btn-bottom:#5e9d17;
  --btn-text:#2f5a12;
  --btn-icon:#3f7215;
  --brand:#4a4a4a;
  --brand-dot:#1d5fa6;
  --label:#111111;
}
*{box-sizing:border-box;margin:0;padding:0}
html,body{width:1200px;height:1200px;overflow:hidden;background:var(--page)}
body{font-family:"Arimo",Arial,sans-serif}
.sheet{position:absolute;left:0;top:0;width:850px;height:850px;transform:scale(1.41176);transform-origin:0 0}

.ad{position:absolute;overflow:hidden;border:1px solid #3a6fa5;
  background:linear-gradient(to bottom,var(--sky) 0,var(--sky-deep) var(--sky-end),var(--leaf) var(--sky-end),var(--paper) var(--leaf-end))}
.size-label{position:absolute;font-size:14px;color:var(--label);white-space:nowrap}

.headline{position:absolute;text-align:center;color:var(--ink-title);font-weight:700;text-transform:uppercase;line-height:1.12;text-shadow:0 1px 0 rgba(255,255,255,.35)}
.offer{position:absolute;background:var(--panel);color:var(--panel-text);font-weight:700;text-align:center;line-height:1.1;display:flex;align-items:center;justify-content:center;border-radius:3px 3px 0 0}
.ribbon-corner{position:absolute;overflow:hidden}
.ribbon{position:absolute;background:linear-gradient(var(--ribbon),var(--ribbon-dark));color:#fff;font-weight:700;text-align:center;transform:rotate(45deg);box-shadow:0 1px 2px rgba(0,0,0,.4)}

.showcase{position:absolute;background:var(--paper)}
.scene{position:absolute;background:linear-gradient(135deg,#e4e7eb,#f6f7f8 55%,#f3c79e);border-radius:2px}
.brand{position:absolute;display:flex;align-items:center;gap:4px;color:var(--brand);font-weight:400;white-space:nowrap}
.brand-dot{border-radius:50%;background:var(--brand-dot)}

.base{position:absolute;left:0;right:0;bottom:0;background:linear-gradient(var(--base),var(--base-deep))}
.base::before{content:"";position:absolute;left:-15%;width:130%;background:var(--paper);border-radius:50%;border-bottom:4px solid var(--rim)}

.cta{position:absolute;display:flex;align-items:center;justify-content:center;gap:10px;border-radius:5px;
  background:linear-gradient(var(--btn-top),var(--btn-bottom));border:1px solid #d7f09a;box-shadow:0 2px 3px rgba(0,0,0,.35);
  color:var(--btn-text);font-weight:700;text-transform:uppercase;text-align:center;line-height:1.05}
.cta-icon{display:flex;align-items:center;justify-content:center;background:var(--btn-icon);border-radius:2px}
.cta-icon svg{display:block}

/* 728 x 90 */
.leaderboard{left:16px;top:10px;width:728px;height:90px;background:linear-gradient(to right,var(--sky) 0,var(--sky-deep) 230px,var(--leaf) 230px,var(--paper) 330px)}
.leaderboard .headline{left:0;top:10px;width:156px;font-size:15px}
.leaderboard .offer{left:156px;top:6px;width:218px;height:78px;font-size:14px;border-radius:3px 0 0 3px}
.leaderboard .ribbon-corner{left:336px;top:0;width:42px;height:42px}
.leaderboard .ribbon{left:2px;top:10px;width:58px;font-size:9px;padding:2px 0}
.leaderboard .showcase{left:374px;top:6px;width:150px;height:78px}
.leaderboard .scene{left:16px;top:26px;width:86px;height:48px}
.leaderboard .brand{left:74px;top:12px;font-size:11px}
.leaderboard .brand-dot{width:8px;height:8px}
.leaderboard .base{left:auto;top:0;width:214px}
.leaderboard .base::before{left:-60px;top:-20%;width:80px;height:140%;border-bottom:0;border-right:4px solid var(--rim)}
.leaderboard .cta{left:555px;top:23px;width:160px;height:45px;font-size:17px}
.leaderboard .cta-icon{width:28px;height:26px}

/* 336 x 280 */
.rectangle{left:12px;top:189px;width:336px;height:280px;--sky-end:58px;--leaf-end:150px}
.rectangle .headline{left:0;top:5px;width:100%;font-size:16px}
.rectangle .offer{left:26px;top:46px;width:284px;height:88px;font-size:19px;padding:0 14px}
.rectangle .ribbon-corner{left:268px;top:44px;width:46px;height:46px}
.rectangle .ribbon{left:2px;top:12px;width:64px;font-size:9px;padding:2px 0}
.rectangle .showcase{left:26px;top:134px;width:284px;height:74px}
.rectangle .scene{left:6px;top:4px;width:176px;height:66px}
.rectangle .brand{left:192px;top:28px;font-size:16px}
.rectangle .brand-dot{width:10px;height:10px}
.rectangle .base{height:72px}
.rectangle .base::before{top:-34px;height:46px}
.rectangle .cta{left:88px;top:227px;width:160px;height:45px;font-size:17px}
.rectangle .cta-icon{width:28px;height:26px}

/* 120 x 600 */
.skyscraper{left:389px;top:129px;width:120px;height:600px;--sky-end:200px;--leaf-end:330px}
.skyscraper .headline{left:0;top:8px;width:100%;font-size:14px;line-height:1.4}
.skyscraper .offer{left:8px;top:120px;width:104px;height:196px;font-size:13px;line-height:1.3;padding:0 4px}
.skyscraper .ribbon-corner{left:78px;top:118px;width:36px;height:36px}
.skyscraper .ribbon{left:0;top:8px;width:52px;font-size:8px;padding:2px 0}
.skyscraper .showcase{left:8px;top:316px;width:104px;height:150px}
.skyscraper .scene{left:4px;top:60px;width:96px;height:86px}
.skyscraper .brand{left:14px;top:20px;font-size:13px}
.skyscraper .brand-dot{width:9px;height:9px}
.skyscraper .base{height:128px}
.skyscraper .base::before{top:-36px;height:52px}
.skyscraper .cta{left:10px;top:515px;width:100px;height:66px;font-size:20px;flex-direction:column;gap:2px}

/* 300 x 600 */
.half-page{left:542px;top:129px;width:300px;height:600px;--sky-end:140px;--leaf-end:340px}
.half-page .headline{left:0;top:12px;width:100%;font-size:22px;line-height:1.1}
.half-page .offer{left:25px;top:92px;width:253px;height:246px;font-size:25px;line-height:1.1;padding:0 20px}
.half-page .ribbon-corner{left:226px;top:90px;width:56px;height:56px}
.half-page .ribbon{left:4px;top:16px;width:76px;font-size:10px;padding:3px 0}
.half-page .showcase{left:25px;top:338px;width:253px;height:150px}
.half-page .scene{left:30px;top:60px;width:196px;height:86px}
.half-page .brand{left:72px;top:18px;font-size:20px}
.half-page .brand-dot{width:12px;height:12px}
.half-page .base{height:110px}
.half-page .base::before{top:-34px;height:52px}
.half-page .cta{left:70px;top:537px;width:160px;height:46px;font-size:17px}
.half-page .cta-icon{width:28px;height:26px}
</style>
</head>
<body>
<main class="sheet">

  <section class="ad leaderboard" aria-label="728 by 90 banner">
    <h2 class="headline">Capture data<br>from<br>handwritten<br>forms</h2>
    <div class="base"></div>
    <p class="offer">Simple, Web Based<br>Solution Digitizes Data,<br>fast 99% accurate</p>
    <div class="showcase">
      <div class="brand"><span class="brand-dot"></span>Formlantic</div>
      <div class="scene" role="img" aria-label="Paper forms turning into data on a computer screen"></div>
    </div>
    <div class="ribbon-corner"><span class="ribbon">FREE</span></div>
    <div class="cta">Try now<span class="cta-icon"><svg width="10" height="12" viewBox="0 0 10 12"><path d="M1 1l8 5-8 5z" fill="#fff"/></svg></span></div>
  </section>
  <p class="size-label" style="left:30px;top:110px">728X90&nbsp; 31.7Kb</p>

  <section class="ad rectangle" aria-label="336 by 280 banner">
    <h2 class="headline">Capture data<br>from handwritten forms</h2>
    <div class="base"></div>
    <p class="offer">Simple, Web Based Solution Digitizes Data, fast 99% accurate</p>
    <div class="showcase">
      <div class="scene" role="img" aria-label="Paper forms turning into data on a computer screen"></div>
      <div class="brand"><span class="brand-dot"></span>Formlantic</div>
    </div>
    <div class="ribbon-corner"><span class="ribbon">FREE</span></div>
    <div class="cta">Try now<span class="cta-icon"><svg width="10" height="12" viewBox="0 0 10 12"><path d="M1 1l8 5-8 5z" fill="#fff"/></svg></span></div>
  </section>
  <p class="size-label" style="left:95px;top:481px">336X280&nbsp; 39.2Kb</p>

  <section class="ad skyscraper" aria-label="120 by 600 banner">
    <h2 class="headline">Capture<br>data<br>from<br>handwritten<br>forms</h2>
    <div class="base"></div>
    <p class="offer">Simple,<br>Web Based<br>Solution<br>Digitizes<br>Data,<br>fast<br>99%<br>accurate</p>
    <div class="showcase">
      <div class="brand"><span class="brand-dot"></span>Formlantic</div>
      <div class="scene" role="img" aria-label="Paper forms turning into data on a computer screen"></div>
    </div>
    <div class="ribbon-corner"><span class="ribbon">FREE</span></div>
    <div class="cta"><span>Try</span><span>now</span></div>
  </section>
  <p class="size-label" style="left:383px;top:740px">120X600&nbsp; 30.0Kb</p>

  <section class="ad half-page" aria-label="300 by 600 banner">
    <h2 class="headline">Capture data<br>from handwritten<br>forms</h2>
    <div class="base"></div>
    <p class="offer">Simple,<br>Web Based<br>Solution<br>Digitizes<br>Data,<br>fast<br>99%<br>accurate</p>
    <div class="showcase">
      <div class="brand"><span class="brand-dot"></span>Formlantic</div>
      <div class="scene" role="img" aria-label="Paper forms turning into data on a computer screen"></div>
    </div>
    <div class="ribbon-corner"><span class="ribbon">FREE</span></div>
    <div class="cta">Try now<span class="cta-icon"><svg width="10" height="12" viewBox="0 0 10 12"><path d="M1 1l8 5-8 5z" fill="#fff"/></svg></span></div>
  </section>
  <p class="size-label" style="left:612px;top:740px">300X600&nbsp; 56.0Kb</p>

</main>
</body>
</html>
```